Billboard for Law Firm

I am looking for a billboard designs. Our branding right now is not good. The logo has to stay the same, but please help come up with something modern, airy, perhaps geometric for the supporting design elements.
Colors should probably be red and blue, or shades of blue, but you can play with the exact shades. Doesn't have to match what you see in the attachment.

The billboard should include:

- Some type of design to bring it to life.

- Logo

- Accident & Injury Law

- 614.355.7182

- Disclaimer (very small text): No Representation Made That The Quality of Legal Services Performed is Greater Than the Those of Other Attorneys

Slogan (very large): Grits, Gravy, and a Good Attorney

______________
Thank You For Your Participation!

Target Market(s)

Southern United States

Industry/Entity Type

Legal Services

Font styles to use
Serif
Sans Serif

Colors
0054AA
0677BA
7BADD7
CADEEF
E8F1F8
EB3D1F
EC4F4E
F09395
F8D3D4
FCEDEE

Requirements
Must have
• Help Make it Memorable and Easy to Read (large text for slogan)
Nice to have
• Some shapes or design elements that may become part of our branding.

```html
<!DOCTYPE html>
<html lang="en">
<head>
<meta charset="UTF-8">
<title>Billboard – Accident &amp; Injury Law</title>
<link rel="stylesheet" href="https://fonts.googleapis.com/css2?family=Poppins:wght@600;800&family=Bebas+Neue&family=Montserrat+Alternates:wght@700&display=swap">
<style>
  :root {
    --red: #c4161c;
    --red-bright: #e0322b;
    --yellow: #f2e600;
    --navy: #0e1a33;
    --white: #ffffff;
    --page: #ffffff;
    --wood-dark: #2a1710;
    --wood-mid: #5a3322;
    --ink: #0e1a33;
    --rule: #c9c9c9;
  }
  html, body {
    margin: 0;
    padding: 0;
    width: 961px;
    height: 1200px;
    overflow: hidden;
    background: var(--page);
  }
  .canvas {
    position: relative;
    width: 961px;
    height: 1200px;
  }
  .billboard {
    position: absolute;
    left: 40px;
    top: 410px;
    width: 880px;
    height: 379px;
    box-shadow: 0 6px 22px rgba(0,0,0,0.22);
  }
  .billboard svg { display: block; }
  .slogan-top {
    font-family: 'Poppins', sans-serif;
    font-weight: 800;
    font-size: 80px;
    fill: var(--white);
  }
  .slogan-main {
    font-family: 'Bebas Neue', 'Oswald', sans-serif;
    font-weight: 400;
    font-size: 128px;
    fill: var(--yellow);
  }
  .practice {
    font-family: 'Poppins', sans-serif;
    font-weight: 800;
    font-size: 48px;
    fill: var(--ink);
  }
  .phone-number {
    font-family: 'Montserrat Alternates', sans-serif;
    font-weight: 700;
    font-size: 72px;
    fill: var(--white);
  }
  .firm-name {
    font-family: 'Poppins', sans-serif;
    font-weight: 600;
    font-size: 30px;
    fill: var(--red);
  }
  .disclaimer {
    font-family: 'Poppins', sans-serif;
    font-weight: 600;
    font-size: 25px;
    fill: var(--ink);
  }
</style>
</head>
<body>
<div class="canvas">
  <div class="billboard">
    <svg viewBox="0 0 1322 569" width="880" height="379" xmlns="http://www.w3.org/2000/svg">
      <defs>
        <linearGradient id="wood" x1="0" y1="0" x2="1" y2="1">
          <stop offset="0" stop-color="#3b2015"/>
          <stop offset="0.5" stop-color="var(--wood-mid)"/>
          <stop offset="1" stop-color="var(--wood-dark)"/>
        </linearGradient>
      </defs>

      <rect class="base" x="0" y="0" width="1322" height="569" fill="var(--white)"/>

      <rect class="slogan-band" x="0" y="0" width="920" height="248" fill="var(--red)"/>

      <path class="phone-band" d="M0 313 L950 313 C990 340 1020 370 1045 410 L0 410 Z" fill="var(--navy)"/>

      <path class="accent-swoosh" d="M1005 325 C1080 370 1140 460 1168 569 L1098 569 C1080 480 1050 400 1005 325 Z" fill="var(--red-bright)"/>

      <path role="img" aria-label="Photo of brass scales of justice on stacked law books in front of a dark wood bookshelf"
            class="hero-photo"
            d="M790 0 C770 90 810 200 900 280 C990 350 1080 390 1125 460 C1150 500 1160 540 1165 569 L1322 569 L1322 0 Z"
            fill="url(#wood)" stroke="var(--white)" stroke-width="8"/>

      <text class="slogan-top" x="55" y="116" textLength="682" lengthAdjust="spacingAndGlyphs">GRITS, GRAVY, &amp;</text>
      <text class="slogan-main" x="59" y="229" textLength="670" lengthAdjust="spacingAndGlyphs">A GOOD ATTORNEY</text>

      <text class="practice" x="59" y="299" textLength="753" lengthAdjust="spacing">ACCIDENT &amp; INJURY LAW</text>

      <g class="phone-icon" transform="translate(87 361)">
        <circle r="28" fill="var(--red-bright)"/>
        <path d="M-10 -12 c-3 0 -5 3 -4 6 c3 10 10 18 20 21 c3 1 6 -1 6 -4 l0 -4 c0 -1 -1 -2 -2 -2 l-6 -1 c-1 0 -2 0 -3 1 l-2 2 c-5 -3 -8 -6 -10 -10 l2 -2 c1 -1 1 -2 1 -3 l-1 -6 c0 -1 -1 -2 -2 -2 Z" fill="var(--white)"/>
      </g>
      <text class="phone-number" x="145" y="387" textLength="774" lengthAdjust="spacingAndGlyphs">614-355-7182</text>

      <circle class="firm-mark" cx="78" cy="482" r="17" fill="var(--red)"/>
      <text class="firm-name" x="106" y="493" textLength="250" lengthAdjust="spacingAndGlyphs">The Harlow Firm</text>
      <line class="divider" x1="381" y1="425" x2="381" y2="515" stroke="var(--rule)" stroke-width="2"/>

      <text class="disclaimer" x="406" y="455" textLength="633" lengthAdjust="spacingAndGlyphs">No Representation Made That The Quality of Legal</text>
      <text class="disclaimer" x="406" y="486" textLength="608" lengthAdjust="spacingAndGlyphs">Services Performed is Greater Than the Those of</text>
      <text class="disclaimer" x="406" y="517">Other Attorneys.</text>
    </svg>
  </div>
</div>
</body>
</html>
```